Home Care App Design

We would like a responsive app design (mobile/web) for an app that will be used by our staff. These need to work display nearly the same for iPhone and Android. The app tracks caregiver tasks (check-in time, daily client activities, caregiver notes, and check out time) and provides updates to team and family members
Updates

I have added individual or grouped pages with better resolution. please let me know if you have any questions

we did not get enough entries so we increase the budget and have not received any new designer entries

Target Market(s)

professional caregivers and family members

Industry/Entity Type

Home Health Care

Font styles to use
Serif

Requirements
Must have
• We currently have a logo - please use colors or slight variants
• We also will need pop-up designs for informational messages and call to actions (with 1-3 options)
Nice to have
• I have attached a sketch of the app, please use this as a guideline. We are looking for ease of use.
• Please feel free to add design aspects that will make it easy to navigate, select options, or enter notes/messages

```html
<!DOCTYPE html>
<html lang="en">
<head>
<meta charset="utf-8">
<title>Kinhaven – Client List</title>
<link href="https://fonts.googleapis.com/css2?family=Roboto:wght@400;500&display=swap" rel="stylesheet">
<style>
:root{
  --page:#cfe6f2;
  --panel:#ffffff;
  --work:#fafbfc;
  --accent:#45718e;
  --accent-strong:#3e7891;
  --muted:#8c9196;
  --line:#e3e6e9;
  --highlight:#e0f3fb;
  --search:#f3f4f6;
  --badge:#3e7891;
}
*{box-sizing:border-box;margin:0;padding:0}
html,body{width:1200px;height:775px;overflow:hidden}
body{background:var(--page);font-family:'Roboto',sans-serif;color:var(--muted);position:relative}
.app{position:absolute;left:0;top:50px;width:1200px;height:675px;background:var(--work);overflow:hidden}
.sidebar{position:absolute;left:0;top:0;width:222px;height:644px;background:var(--panel);border-right:1px solid var(--line)}
.brand{position:absolute;left:20px;top:9px;display:flex;align-items:center;gap:7px;font-size:20px;font-weight:400;color:var(--accent)}
.brand-dot{width:12px;height:12px;border-radius:50%;background:var(--accent)}
.collapse{position:absolute;left:198px;top:16px}
.profile-ring{position:absolute;left:59px;top:59px;width:102px;height:102px;border-radius:50%;background:#f1f2f3}
.profile-photo{position:absolute;left:64px;top:64px;width:92px;height:92px;border-radius:50%;background:radial-gradient(circle at 50% 55%,#d9a07e 0%,#8a5333 55%,#4a2a18 100%)}
.profile-name{position:absolute;left:0;width:222px;top:170px;text-align:center;font-size:17px;font-weight:500;color:var(--accent);letter-spacing:.3px}
.profile-phone{position:absolute;left:0;width:222px;top:196px;text-align:center;font-size:13px;color:var(--muted)}
.nav{position:absolute;left:0;top:240px;width:222px;list-style:none}
.nav li{height:47px;display:flex;align-items:center;padding-left:16px;font-size:14px;font-weight:500;color:var(--muted);position:relative}
.nav li svg{width:22px;height:22px;margin-right:24px;stroke:var(--muted);fill:none;stroke-width:1.4}
.nav li.active{background:var(--highlight);color:var(--accent)}
.nav li.active::before{content:"";position:absolute;left:0;top:0;bottom:0;width:3px;background:var(--accent-strong)}
.nav li.active svg{stroke:var(--accent)}
.topbar{position:absolute;left:222px;top:0;width:978px;height:46px;background:var(--panel);box-shadow:0 2px 6px rgba(0,0,0,.05)}
.page-title{position:absolute;left:26px;top:12px;font-size:18px;font-weight:500;color:var(--accent);letter-spacing:.3px}
.search{position:absolute;left:269px;top:9px;width:436px;height:29px;border-radius:15px;background:var(--search);display:flex;align-items:center;padding-left:16px;font-size:14px;color:#b3b7bb}
.search svg{margin-right:12px}
.top-icons svg{position:absolute;top:12px;fill:none;stroke:var(--accent);stroke-width:1.4}
.badge{position:absolute;left:830px;top:7px;width:14px;height:14px;border-radius:50%;background:var(--badge);color:#fff;font-size:9px;text-align:center;line-height:14px}
.sort-label{position:absolute;left:960px;top:68px;font-size:14px;color:var(--muted)}
.sort-select{position:absolute;left:1020px;top:60px;width:153px;height:33px;border:1px solid var(--line);border-radius:3px;background:var(--panel);display:flex;align-items:center;justify-content:space-between;padding:0 12px;font-size:14px;color:var(--muted)}
.client-card{position:absolute;width:455px;height:94px;background:var(--panel);border:1px solid var(--line);border-radius:2px}
.client-photo{position:absolute;left:18px;top:23px;width:48px;height:48px;border-radius:50%}
.client-name{position:absolute;left:82px;top:14px;font-size:17px;font-weight:500;color:var(--accent)}
.client-address{position:absolute;left:82px;top:44px;font-size:12px;line-height:16px;color:var(--muted)}
.client-meta{position:absolute;left:292px;top:14px;font-size:14.5px;line-height:21px;color:var(--muted)}
.client-meta b{font-weight:500;color:var(--accent)}
.footer{position:absolute;left:0;top:644px;width:1200px;height:31px;background:var(--accent-strong);color:#fff;font-size:12px;display:flex;justify-content:center;align-items:center;gap:10px}
.footer .soft{opacity:.7}
</style>
</head>
<body>
<div class="app">

  <aside class="sidebar">
    <div class="brand"><span class="brand-dot"></span>Kinhaven</div>
    <svg class="collapse" width="10" height="14" viewBox="0 0 10 14"><path d="M8 1 2 7l6 6" fill="none" stroke="#45718e" stroke-width="1.8"/></svg>
    <div class="profile-ring"></div>
    <div class="profile-photo" role="img" aria-label="Portrait photo of the signed-in caregiver"></div>
    <div class="profile-name">MARA ELLIS</div>
    <div class="profile-phone">(555)014-2231</div>
    <ul class="nav">
      <li><svg viewBox="0 0 24 24"><path d="M3 4h18v12H9l-5 4v-4H3z"/><circle cx="8" cy="10" r=".6"/><circle cx="12" cy="10" r=".6"/><circle cx="16" cy="10" r=".6"/></svg>Messages</li>
      <li class="active"><svg viewBox="0 0 24 24"><circle cx="8" cy="7" r="3.5"/><circle cx="16" cy="7" r="3.5"/><path d="M2 20c0-4 3-7 6-7s6 3 6 7M10 20c0-4 3-7 6-7s6 3 6 7"/></svg>Families</li>
      <li><svg viewBox="0 0 24 24"><circle cx="12" cy="7" r="3.5"/><circle cx="5" cy="9" r="2.5"/><circle cx="19" cy="9" r="2.5"/><path d="M6 20c0-4 3-7 6-7s6 3 6 7M1 18c0-3 2-5 4-5M23 18c0-3-2-5-4-5"/></svg>Team</li>
      <li><svg viewBox="0 0 24 24"><path d="M12 3a9 9 0 1 1-9 9"/><path d="M12 7v5h4M3 8l2-4"/></svg>Time Cards</li>
      <li><svg viewBox="0 0 24 24"><circle cx="12" cy="12" r="3.5"/><path d="M12 2l2 3 3-1 1 3 3 1-1 3 3 2-3 2 1 3-3 1-1 3-3-1-2 3-2-3-3 1-1-3-3-1 1-3-3-2 3-2-1-3 3-1 1-3 3 1z"/></svg>Settings</li>
      <li><svg viewBox="0 0 24 24"><rect x="4" y="10" width="16" height="12" rx="1"/><path d="M8 10V7a4 4 0 0 1 8 0v3"/><circle cx="12" cy="16" r="2"/></svg>Privacy &amp; Policy</li>
      <li><svg viewBox="0 0 24 24"><circle cx="12" cy="12" r="10"/><path d="M12 6v8M12 17v1"/></svg>About</li>
      <li><svg viewBox="0 0 24 24"><path d="M7 5a9 9 0 1 0 10 0M12 2v10"/></svg>Logout</li>
    </ul>
  </aside>

  <header class="topbar">
    <h1 class="page-title">CLIENT LIST</h1>
    <div class="search">
      <svg width="15" height="15" viewBox="0 0 16 16"><circle cx="6.5" cy="6.5" r="5.5" fill="none" stroke="#8c9196" stroke-width="1.4"/><path d="M10.5 10.5 15 15" stroke="#8c9196" stroke-width="1.4"/></svg>
      Search here
    </div>
    <div class="top-icons">
      <svg style="left:815px" width="20" height="22" viewBox="0 0 20 22"><path d="M4 16V9a6 6 0 0 1 12 0v7l2 2H2zM8 20h4"/></svg>
      <svg style="left:883px" width="22" height="20" viewBox="0 0 22 20"><rect x="1.5" y="3.5" width="19" height="13"/><path d="M1.5 3.5 11 11l9.5-7.5"/></svg>
      <svg style="left:940px" width="21" height="21" viewBox="0 0 21 21"><circle cx="10.5" cy="10.5" r="9.5"/><path d="M10.5 9v6M10.5 6v1"/></svg>
    </div>
    <div class="badge">3</div>
  </header>

  <div class="sort-label">Sort by:</div>
  <div class="sort-select">Lorem Ipsum
    <svg width="10" height="6" viewBox="0 0 10 6"><path d="M1 1l4 4 4-4" fill="none" stroke="#45718e" stroke-width="1.4"/></svg>
  </div>

  <article class="client-card" style="left:248px;top:114px">
    <div class="client-photo" role="img" aria-label="Client photo" style="background:linear-gradient(135deg,#c9b6a6,#3b3b3f)"></div>
    <div class="client-name">Jhon doe</div>
    <div class="client-address">48 Linden Row<br>Brookfield. VT 05000</div>
    <div class="client-meta"><b>Program:</b> Home Care<br><b>DOB:</b> 2/1/1938 <b>Age:</b> 88<br><b>Phone:</b> (555) 014-2231</div>
  </article>
  <article class="client-card" style="left:718px;top:114px">
    <div class="client-photo" role="img" aria-label="Client photo" style="background:linear-gradient(135deg,#7a5c48,#d8a88a)"></div>
    <div class="client-name">Fang Williams</div>
    <div class="client-address">48 Linden Row<br>Brookfield. VT 05000</div>
    <div class="client-meta"><b>Program:</b> Home Care<br><b>DOB:</b> 2/1/1938 <b>Age:</b> 88<br><b>Phone:</b> (555) 014-2231</div>
  </article>

  <article class="client-card" style="left:248px;top:217px">
    <div class="client-photo" role="img" aria-label="Client photo" style="background:linear-gradient(135deg,#5a3524,#d39a78)"></div>
    <div class="client-name">Aaliyah Watson</div>
    <div class="client-address">48 Linden Row<br>Brookfield. VT 05000</div>
    <div class="client-meta"><b>Program:</b> Home Care<br><b>DOB:</b> 2/1/1938 <b>Age:</b> 88<br><b>Phone:</b> (555) 014-2231</div>
  </article>
  <article class="client-card" style="left:718px;top:217px">
    <div class="client-photo" role="img" aria-label="Client photo" style="background:linear-gradient(135deg,#2f2a26,#c08f70)"></div>
    <div class="client-name">Gael Thompson</div>
    <div class="client-address">48 Linden Row<br>Brookfield. VT 05000</div>
    <div class="client-meta"><b>Program:</b> Home Care<br><b>DOB:</b> 2/1/1938 <b>Age:</b> 88<br><b>Phone:</b> (555) 014-2231</div>
  </article>

  <article class="client-card" style="left:248px;top:320px">
    <div class="client-photo" role="img" aria-label="Client photo" style="background:linear-gradient(135deg,#4a3426,#e0a788)"></div>
    <div class="client-name">Addison Smith</div>
    <div class="client-address">48 Linden Row<br>Brookfield. VT 05000</div>
    <div class="client-meta"><b>Program:</b> Home Care<br><b>DOB:</b> 2/1/1938 <b>Age:</b> 88<br><b>Phone:</b> (555) 014-2231</div>
  </article>
  <article class="client-card" style="left:718px;top:320px">
    <div class="client-photo" role="img" aria-label="Client photo" style="background:linear-gradient(135deg,#5b4a3e,#2c2320)"></div>
    <div class="client-name">Jack Parker</div>
    <div class="client-address">48 Linden Row<br>Brookfield. VT 05000</div>
    <div class="client-meta"><b>Program:</b> Home Care<br><b>DOB:</b> 2/1/1938 <b>Age:</b> 88<br><b>Phone:</b> (555) 014-2231</div>
  </article>

  <article class="client-card" style="left:248px;top:423px">
    <div class="client-photo" role="img" aria-label="Client photo" style="background:linear-gradient(135deg,#6d6a5a,#caa38c)"></div>
    <div class="client-name">Eadric Williams</div>
    <div class="client-address">48 Linden Row<br>Brookfield. VT 05000</div>
    <div class="client-meta"><b>Program:</b> Home Care<br><b>DOB:</b> 2/1/1938 <b>Age:</b> 88<br><b>Phone:</b> (555) 014-2231</div>
  </article>
  <article class="client-card" style="left:718px;top:423px">
    <div class="client-photo" role="img" aria-label="Client photo" style="background:linear-gradient(135deg,#e4a6c4,#f2d2bf)"></div>
    <div class="client-name">Maaria Collins</div>
    <div class="client-address">48 Linden Row<br>Brookfield. VT 05000</div>
    <div class="client-meta"><b>Program:</b> Home Care<br><b>DOB:</b> 2/1/1938 <b>Age:</b> 88<br><b>Phone:</b> (555) 014-2231</div>
  </article>

  <article class="client-card" style="left:248px;top:526px">
    <div class="client-photo" role="img" aria-label="Client photo" style="background:linear-gradient(135deg,#1f1a18,#e8c4b0)"></div>
    <div class="client-name">Easter O neill</div>
    <div class="client-address">48 Linden Row<br>Brookfield. VT 05000</div>
    <div class="client-meta"><b>Program:</b> Home Care<br><b>DOB:</b> 2/1/1938 <b>Age:</b> 88<br><b>Phone:</b> (555) 014-2231</div>
  </article>
  <article class="client-card" style="left:718px;top:526px">
    <div class="client-photo" role="img" aria-label="Client photo" style="background:linear-gradient(135deg,#4a3b30,#c9a187)"></div>
    <div class="client-name">Paavo Wells</div>
    <div class="client-address">48 Linden Row<br>Brookfield. VT 05000</div>
    <div class="client-meta"><b>Program:</b> Home Care<br><b>DOB:</b> 2/1/1938 <b>Age:</b> 88<br><b>Phone:</b> (555) 014-2231</div>
  </article>

  <article class="client-card" style="left:248px;top:629px"></article>
  <article class="client-card" style="left:718px;top:629px"></article>

  <footer class="footer"><span><span class="soft">Copyright ©</span> All rights reserved</span><span class="soft">|</span><span>Kinhaven</span></footer>
</div>
</body>
</html>
```